Print materials for 3-star hotel

We are changing up our print materials (notepads, letterheads, key card jackets, small flyer for the room rates) We are a 3 star business hotel in the Philippines and have mainly used grey tones and clean, simple lines. See attached photos for logo and hotel interior photos.

Target Market(s)

Business

Contact Information for Business Card

Corvina Terrace Hotel
Magistrate Lunod Avenue corner Pabilo St Cebu City 6000 Philippines
Tel: +63 32 481 7520
Mobile: +63 917 604 2893
www.corvinaterracehotel.example

Font styles to use
Serif
Sans Serif

Requirements
Must have
• Simple
• Readable font and font size
Nice to have
• Neutral colors, grey and taupes
Should not have
• No purples and bright blues

```html
<!DOCTYPE html>
<html lang="en">
<head>
<meta charset="utf-8">
<title>Corvina Terrace Hotel — Stationery Set</title>
<link rel="stylesheet" href="https://fonts.googleapis.com/css2?family=Cinzel:wght@400&family=Questrial&family=Roboto:wght@400;700&display=swap">
<style>
  :root{
    --backdrop:#dedede;
    --paper:#f3f3f3;
    --paper-white:#f7f7f7;
    --ink:#1a1a1a;
    --folder:#1c1c1c;
    --folder-spine:#141414;
    --band-grey:#b4b4b4;
    --text-grey:#4a4a4a;
    --soft-grey:#d6d6d6;
    --white:#ffffff;
  }
  *{margin:0;padding:0;box-sizing:border-box}
  html,body{width:1200px;height:899px;overflow:hidden;background:var(--backdrop)}
  address{font-style:normal}
  .canvas{position:relative;width:1200px;height:899px;background:var(--backdrop);font-family:"Questrial",sans-serif;color:var(--ink)}

  .brand{font-family:"Cinzel",serif;font-weight:400;text-align:center;color:var(--ink);line-height:1}
  .brand__name{display:block;letter-spacing:.18em;white-space:nowrap}
  .brand__sub{display:block;letter-spacing:.35em}

  /* Letterhead */
  .letterhead{position:absolute;left:152px;top:80px;width:378px;height:532px;background:var(--paper);overflow:hidden}
  .letterhead .brand{position:absolute;left:26px;top:60px;width:96px}
  .letterhead .brand__name{font-size:7px}
  .letterhead .brand__sub{font-size:4.5px;margin-top:3px}
  .contact-block{position:absolute;left:274px;top:30px;padding-left:6px;border-left:1px solid var(--soft-grey);font-size:5.2px;line-height:7px;color:var(--text-grey);white-space:nowrap}
  .contact-block .gap{height:3px}
  .contact-row{display:flex;align-items:center;gap:3px;white-space:nowrap}
  .contact-row svg{width:5px;height:5px;flex:none}
  .letter{position:absolute;left:33px;top:150px;width:316px;color:var(--text-grey)}
  .letter__greeting{font-size:9.5px;color:#333;margin-bottom:14px}
  .letter p{font-size:5.3px;line-height:8.1px;text-align:justify;margin-bottom:8px}
  .letter__closing{margin-top:14px}
  .signature{width:70px;height:24px;margin-top:8px;background:var(--soft-grey);border-radius:3px}
  .paper-footer{position:absolute;left:0;bottom:0;width:100%;height:20px}
  .paper-footer__url{position:absolute;right:14px;bottom:8px;font-size:5px;line-height:6px;letter-spacing:.2em;color:var(--white);white-space:nowrap}

  /* Folder */
  .folder{position:absolute;left:564px;top:48px;width:445px;height:565px;background:var(--folder)}
  .folder__spine{position:absolute;left:0;top:0;width:24px;height:100%;background:var(--folder-spine);border-right:1px solid #2a2a2a}
  .folder__spine::before,.folder__spine::after{content:"";position:absolute;top:0;width:1px;height:100%;background:#2e2e2e}
  .folder__spine::before{left:8px}.folder__spine::after{left:16px}
  .folder .brand{position:absolute;left:24px;right:0;top:286px;color:var(--white)}
  .folder .brand__name{font-size:17px}
  .folder .brand__sub{font-size:11px;margin-top:8px}

  /* Business cards */
  .card{position:absolute;left:67px;width:157px;height:90px;overflow:hidden}
  .card--front{top:656px;background:var(--folder)}
  .card--front .brand{position:absolute;left:0;right:0;top:40px;color:var(--white)}
  .card--front .brand__name{font-size:6px}
  .card--front .brand__sub{font-size:3.8px;margin-top:2px}
  .card__url{position:absolute;left:0;right:0;bottom:12px;text-align:center;font-size:4px;letter-spacing:.3em;color:#cfcfcf;white-space:nowrap}
  .card--back{top:762px;background:var(--paper-white)}
  .card--back .brand{position:absolute;right:10px;top:26px;width:66px}
  .card--back .brand__name{font-size:5px}
  .card--back .brand__sub{font-size:3.4px;margin-top:2px}
  .card__person{position:absolute;left:10px;top:38px;font-family:"Roboto",sans-serif}
  .card__person strong{display:block;font-size:5.6px;font-weight:700;letter-spacing:.02em}
  .card__person span{display:block;font-size:3.4px;color:var(--text-grey);margin-top:1px}
  .card__rule{position:absolute;left:10px;right:10px;top:53px;height:1px;background:var(--soft-grey)}
  .card__contacts{position:absolute;left:10px;top:57px;font-size:3.5px;line-height:5px;color:var(--text-grey)}
  .card__contacts .contact-row svg{width:3.5px;height:3.5px}
  .card__address{position:absolute;right:10px;top:67px;font-size:3.5px;line-height:5px;text-align:right;color:var(--text-grey);white-space:nowrap}
  .card--back .paper-footer{height:10px}
  .card--back .paper-footer__url{font-size:3.4px;line-height:4px;right:6px;bottom:1px;letter-spacing:.1em}

  /* Envelope front */
  .envelope-front{position:absolute;left:242px;top:656px;width:436px;height:197px;background:var(--paper)}
  .envelope-front .brand{position:absolute;left:24px;top:29px;width:84px}
  .envelope-front .brand__name{font-size:6.4px}
  .envelope-front .brand__sub{font-size:4.2px;margin-top:2px}
  .envelope-front__address{position:absolute;left:24px;top:66px;width:84px;text-align:center;font-family:"Roboto",sans-serif;font-size:5.8px;line-height:8px;color:#333}
  .envelope-front .paper-footer{height:16px}

  /* Envelope back */
  .envelope-back{position:absolute;left:700px;top:654px;width:436px;height:199px;background:var(--paper-white)}
  .envelope-back svg{position:absolute;left:0;top:0}
  .envelope-back .brand{position:absolute;left:0;right:0;top:27px;color:var(--white)}
  .envelope-back .brand__name{font-size:9px}
</style>
</head>
<body>
<div class="canvas">

  <article class="letterhead">
    <div class="brand"><span class="brand__name">Corvina Terrace</span><span class="brand__sub">Hotel</span></div>
    <address class="contact-block">
      <div>Magistrate Lunod Avenue corner</div>
      <div>Pabilo St, Cebu City 6000</div>
      <div class="gap"></div>
      <div class="contact-row"><svg viewBox="0 0 10 10"><path d="M2 1h2l1 2-1 1a6 6 0 0 0 2 2l1-1 2 1v2l-1 1C4 9 1 6 1 2z" fill="#1a1a1a"/></svg>+63 32 481 7520</div>
      <div class="contact-row"><svg viewBox="0 0 10 10"><rect x="2.5" y="0.5" width="5" height="9" rx="1" fill="none" stroke="#1a1a1a" stroke-width="1.2"/></svg>+63 917 604 2893</div>
      <div class="contact-row"><svg viewBox="0 0 10 10"><rect x="1" y="4" width="8" height="5" fill="#1a1a1a"/><rect x="3" y="1" width="4" height="3" fill="#1a1a1a"/></svg>+63 32 481 7521</div>
      <div class="contact-row"><svg viewBox="0 0 10 10"><rect x="1" y="2" width="8" height="6" fill="#1a1a1a"/></svg>stay@corvinaterracehotel.example</div>
    </address>
    <section class="letter">
      <div class="letter__greeting">Dear Mr. Valdez,</div>
      <p>Thank you for choosing our hotel for your upcoming business stay in Cebu City. We are pleased to confirm your reservation and have arranged a quiet room on an upper floor, close to the lift and the business lounge, as you requested in your note.</p>
      <p>Breakfast is served daily from six until ten in the lobby restaurant. Our front desk is open at all hours and can help with airport transfers, meeting rooms, printing and local transport for your team during the week.</p>
      <p>Should you need a late check-out or any change to your booking, please contact us by phone or email and we will gladly make the arrangements. Wireless internet is included in every room and in all shared spaces of the hotel.</p>
      <p>We look forward to welcoming you and hope your stay with us is a comfortable and productive one.</p>
      <p class="letter__closing">Sincerely,</p>
      <div class="signature" role="img" aria-label="Handwritten signature"></div>
    </section>
    <svg class="paper-footer" viewBox="0 0 378 20" preserveAspectRatio="none">
      <rect x="0" y="6" width="222" height="4" fill="var(--band-grey)"/>
      <rect x="0" y="12" width="378" height="8" fill="var(--ink)"/>
      <path d="M236 0H378V12H226Z" fill="var(--ink)"/>
    </svg>
    <span class="paper-footer__url">www.corvinaterracehotel.example</span>
  </article>

  <section class="folder">
    <div class="folder__spine"></div>
    <div class="brand"><span class="brand__name">Corvina Terrace</span><span class="brand__sub">Hotel</span></div>
  </section>

  <article class="card card--front">
    <div class="brand"><span class="brand__name">Corvina Terrace</span><span class="brand__sub">Hotel</span></div>
    <div class="card__url">www.corvinaterracehotel.example</div>
  </article>

  <article class="card card--back">
    <div class="brand"><span class="brand__name">Corvina Terrace</span><span class="brand__sub">Hotel</span></div>
    <div class="card__person"><strong>ELENA MARQUEZ</strong><span>CEO/FOUNDER</span></div>
    <div class="card__rule"></div>
    <div class="card__contacts">
      <div class="contact-row"><svg viewBox="0 0 10 10"><path d="M2 1h2l1 2-1 1a6 6 0 0 0 2 2l1-1 2 1v2l-1 1C4 9 1 6 1 2z" fill="#1a1a1a"/></svg>+63 32 481 7520</div>
      <div class="contact-row"><svg viewBox="0 0 10 10"><rect x="2.5" y="0.5" width="5" height="9" rx="1" fill="none" stroke="#1a1a1a" stroke-width="1.2"/></svg>+63 917 604 2893</div>
      <div class="contact-row"><svg viewBox="0 0 10 10"><rect x="1" y="4" width="8" height="5" fill="#1a1a1a"/><rect x="3" y="1" width="4" height="3" fill="#1a1a1a"/></svg>+63 32 481 7521</div>
      <div class="contact-row"><svg viewBox="0 0 10 10"><rect x="1" y="2" width="8" height="6" fill="#1a1a1a"/></svg>stay@corvinaterrace.example</div>
    </div>
    <address class="card__address"><div>Magistrate Lunod Ave cor. Pabilo St</div><div>Cebu City 6000</div></address>
    <svg class="paper-footer" viewBox="0 0 157 10" preserveAspectRatio="none">
      <rect x="0" y="3" width="64" height="2" fill="var(--band-grey)"/>
      <rect x="0" y="6" width="157" height="4" fill="var(--ink)"/>
      <path d="M72 0H157V6H68Z" fill="var(--ink)"/>
    </svg>
    <span class="paper-footer__url">www.corvinaterracehotel.example</span>
  </article>

  <article class="envelope-front">
    <div class="brand"><span class="brand__name">Corvina Terrace</span><span class="brand__sub">Hotel</span></div>
    <address class="envelope-front__address"><div>PO Box 2417</div><div>Cebu City 6000</div></address>
    <svg class="paper-footer" viewBox="0 0 436 16" preserveAspectRatio="none">
      <rect x="0" y="3" width="310" height="3" fill="var(--band-grey)"/>
      <rect x="0" y="9" width="436" height="7" fill="var(--ink)"/>
      <path d="M320 0H436V9H310Z" fill="var(--ink)"/>
    </svg>
  </article>

  <article class="envelope-back">
    <svg width="436" height="64" viewBox="0 0 436 64">
      <path d="M0 0H436C436 10 431 14 429 22L425 44Q421 62 401 62H35Q15 62 11 44L7 22C5 14 0 10 0 0Z" fill="var(--ink)"/>
    </svg>
    <div class="brand"><span class="brand__name">Corvina Terrace</span></div>
  </article>

</div>
</body>
</html>
```